Homemaking training schools needs a Business Card design

Designer, Hello!

No special requirements, good-looking enough.
--------------------------------------------------------------------------

Name: Marcus Liao
Chairman
Tel: 0574-57418263
Mobile: 13852247106
Email: kelvory@mailpond.com
Web: www.tqb2031.com
Add: No.258, LinfengJie, DaoyueQu, Ningbo, Zhejiang

LOGO
Ningbo TQB Homemaking Training School

Target Market(s)

pregnant women, mothers, infants, the elderly and families, including cleaning, cooking, nursing training.

Industry/Entity Type

Business

Contact Information for Business Card

Name: Marcus Liao
Chairman
Tel: 0574-57418263
Mobile: 13852247106
Email: kelvory@mailpond.com
Web: www.tqb2031.com

LOGO

Font styles to use
Serif
Sans Serif
Decorative

Requirements
Nice to have
• Feels: clean, specifications, safety, comfort, warmth and happiness.

```html
<!DOCTYPE html>
<html lang="en">
<head>
<meta charset="utf-8">
<title>Tianqing Training Business Card</title>
<link href="https://fonts.googleapis.com/css2?family=Lato:wght@400;700;900&display=swap" rel="stylesheet">
<style>
  :root {
    --page: #e9e6e2;
    --white: #ffffff;
    --blue: #1f78c8;
    --blue-light: #3a9ae0;
    --dark: #1b1b1d;
    --dark-mid: #3a3a3d;
    --ink: #2a2a2e;
    --text-light: #f2f2f2;
  }
  * { margin: 0; padding: 0; box-sizing: border-box; }
  html, body { width: 1200px; height: 913px; overflow: hidden; }
  body { background: var(--page); font-family: "Lato", sans-serif; position: relative; }

  .card {
    position: absolute; left: 290px; width: 620px; height: 354px;
    overflow: hidden; box-shadow: 0 10px 28px rgba(0,0,0,.22);
  }
  .card--front { top: 70px; background: var(--white); }
  .card--back { top: 489px; background: linear-gradient(160deg, var(--dark-mid) 0%, var(--dark) 55%, #0e0e10 100%); }

  .card__shape { position: absolute; inset: 0; width: 100%; height: 100%; }

  .brand { position: absolute; display: flex; align-items: center; gap: 12px; }
  .brand__mark { width: 14px; height: 14px; background: var(--blue); flex: none; }
  .brand__name { font-weight: 700; color: var(--ink); font-size: 30px; letter-spacing: 1px; white-space: nowrap; }
  .card--front .brand { right: 48px; top: 62px; }
  .card--back .brand { left: 40px; top: 219px; }
  .card--back .brand__name { font-size: 28px; }

  .holder { position: absolute; left: 38px; top: 150px; color: var(--white); }
  .holder__name { font-weight: 900; font-size: 28px; letter-spacing: .5px; text-transform: uppercase; }
  .holder__name span { font-weight: 400; }
  .holder__role { font-size: 17px; margin-top: 2px; }

  .contact { position: absolute; left: 170px; top: 230px; color: var(--text-light); font-size: 14px; }
  .contact__address { margin-bottom: 12px; }
  .contact__grid { display: grid; grid-template-columns: 190px auto; row-gap: 9px; column-gap: 20px; }
  .contact__item { display: flex; align-items: center; gap: 9px; }
  .icon { width: 20px; height: 20px; background: var(--blue); border-radius: 4px; display: flex; align-items: center; justify-content: center; flex: none; }
  .icon svg { width: 14px; height: 14px; }

  .web-band { position: absolute; right: 0; top: 118px; width: 290px; height: 118px; display: flex; align-items: center; justify-content: center; color: var(--white); font-weight: 700; font-size: 24px; }
</style>
</head>
<body>

<section class="card card--front" aria-label="Card front">
  <svg class="card__shape" viewBox="0 0 620 354" aria-hidden="true">
    <defs>
      <linearGradient id="darkBand" x1="0" y1="0" x2="1" y2="1">
        <stop offset="0" stop-color="#3d3d40"/>
        <stop offset="1" stop-color="#141416"/>
      </linearGradient>
      <linearGradient id="blueBand" x1="0" y1="0" x2="1" y2="0">
        <stop offset="0" stop-color="#1a64b4"/>
        <stop offset="1" stop-color="#3a9ae0"/>
      </linearGradient>
    </defs>
    <polygon points="230,150 620,150 620,326 150,326 150,215" fill="url(#darkBand)"/>
    <rect x="520" y="158" width="84" height="70" rx="12" fill="#2b2b2e" stroke="#1f78c8" stroke-width="3"/>
    <polygon points="0,132 270,132 310,212 0,212" fill="url(#blueBand)"/>
  </svg>

  <div class="brand">
    <span class="brand__mark"></span>
    <span class="brand__name">Tianqing Training</span>
  </div>

  <div class="holder">
    <div class="holder__name">Marcus <span>Liao</span></div>
    <div class="holder__role">Chairman</div>
  </div>

  <div class="contact">
    <p class="contact__address">258, LinfengJie, DaoyueQu, Ningbo, Zhejiang</p>
    <div class="contact__grid">
      <div class="contact__item">
        <span class="icon"><svg viewBox="0 0 14 14"><path d="M3 1.5l2 2.6-1.2 1.3c.8 1.7 2 2.9 3.8 3.8L8.9 8l2.6 2-1 2.3C6 12.3 1.7 8 1.7 2.5z" fill="#fff"/></svg></span>
        <span>0574-57418263</span>
      </div>
      <div class="contact__item">
        <span class="icon"><svg viewBox="0 0 14 14"><rect x="1.5" y="3" width="11" height="8" rx="1" fill="#fff"/><path d="M1.8 3.4L7 7.6l5.2-4.2" stroke="#1f78c8" stroke-width="1.2" fill="none"/></svg></span>
        <span>kelvory@mailpond.com</span>
      </div>
      <div class="contact__item">
        <span class="icon"><svg viewBox="0 0 14 14"><rect x="4" y="1" width="6" height="12" rx="1.2" fill="#fff"/><circle cx="7" cy="11" r=".8" fill="#1f78c8"/></svg></span>
        <span>13852247106</span>
      </div>
      <div class="contact__item">
        <span class="icon"><svg viewBox="0 0 14 14" fill="none" stroke="#fff" stroke-width="1.1"><circle cx="7" cy="7" r="5.5"/><ellipse cx="7" cy="7" rx="2.4" ry="5.5"/><path d="M1.5 7h11"/></svg></span>
        <span>www.tqb2031.com</span>
      </div>
    </div>
  </div>
</section>

<section class="card card--back" aria-label="Card back">
  <svg class="card__shape" viewBox="0 0 620 354" aria-hidden="true">
    <defs>
      <linearGradient id="webBand" x1="0" y1="0" x2="1" y2="0">
        <stop offset="0" stop-color="#3a9ae0"/>
        <stop offset="1" stop-color="#1f88d6"/>
      </linearGradient>
    </defs>
    <rect x="0" y="180" width="330" height="118" fill="#fff"/>
    <rect x="330" y="118" width="290" height="118" fill="url(#webBand)"/>
  </svg>

  <div class="brand">
    <span class="brand__mark"></span>
    <span class="brand__name">Tianqing Training</span>
  </div>

  <div class="web-band">www.tqb2031.com</div>
</section>

</body>
</html>
```